poster design for a sales competition

we are requiring a series of posters for sales competitions. The posters should reflect that it is a race and there is a winner, so the poster imagery will motivate the sales team to sell more,
the posters will require blank fields for names of the contestants and space for progressive scores/tally
suggestions: racetrack ie horse/car/track and field etc.or a graph or anything that has a start and finish
eg if it is a race maybe stands around the border of the track.
the blank fields will accomodate 10-12 contestants and as such will need their own lanes that can be filled in as they progress over the sales competition period,another idea is perhaps at the bottom of the poster you could have a series of cutouts eg car race theme colour coded race cars that once cut out could be blue tacked to the poster to create a 2D image and competition position around the track./

we are requiring several different themes and designs and will offer 2nd and 3rd place payments and more if we recieve a number of satisfactory designs

Target Market(s)

the audience is highly motivated sales peoplefrom your design and others i know my concept is difficult to get so i'll try and explain the poster is a race between sales persons(SP) if you have a 10 week sales contest and 8 (SP) the first week one (SP) sells $5000 and one sells $4000 one sells $2000 etc the one who sells most will be the leader in the pool each week they will progress up the pool over the 10 weeks until the end and the winner is the leader, the poster is avisual of their performance against the other (SP)

Industry/Entity Type

Progressive

Requirements
Must have
• start and finish
blank fields for weekly/daily sales results
blank fields for the sales teams names
size is A1 or A0
images to be free of copyright
Nice to have
• should have a theme
can have cut outs
can have space for competition start and finish dates

```html
<!DOCTYPE html>
<html lang="en">
<head>
<meta charset="utf-8">
<title>Lap Leaders Race – Sales Race Poster</title>
<link rel="stylesheet" href="https://fonts.googleapis.com/css2?family=Roboto:wght@400;500&display=swap">
<style>
  :root {
    --band: #000000;
    --paper: #ffffff;
    --ink: #1a1a1a;
    --panel-blue: #2e4a9e;
    --tag-yellow: #f5e616;
    --pool-navy: #253685;
    --water: #56c2e2;
    --lane-blue: #1f7fc4;
    --rope-red: #e0262b;
    --rope-orange: #e07b24;
    --warning-red: #f0646a;
    --title-blue: #1f7fd0;
    --trophy-gold: #e6b422;
    --flag-grey: #555555;
    --whistle-grey: #8a8a8a;
  }
  html, body { margin: 0; padding: 0; width: 1200px; height: 1200px; overflow: hidden; background: var(--band); }
  .poster { display: block; width: 1200px; height: 1200px; }
  .canvas-bg { fill: var(--paper); }
  .band { fill: var(--band); }
  .frame { fill: none; stroke: var(--ink); stroke-width: 1.3; }
  .fold-line { fill: none; stroke: var(--ink); stroke-width: 0.8; stroke-dasharray: 3 2; }
  .title { font-family: "Roboto", sans-serif; font-weight: 500; font-size: 20px; fill: var(--title-blue); letter-spacing: 0.5px; }
  .tag { fill: var(--tag-yellow); stroke: #c9bb00; stroke-width: 0.5; }
  .tag-label { font-family: "Roboto", sans-serif; font-size: 7px; font-weight: 500; fill: var(--ink); }
  .side-panel { fill: var(--panel-blue); }
  .entry-field { fill: var(--paper); stroke: #9aa4c8; stroke-width: 0.6; }
  .week-num { font-family: "Roboto", sans-serif; font-size: 7px; fill: var(--ink); }
  .pool-surround { fill: var(--paper); stroke: var(--ink); stroke-width: 0.9; }
  .pool-edge { fill: var(--pool-navy); }
  .pool-lip { fill: none; stroke: #c9d7ee; stroke-width: 1.5; }
  .water { fill: var(--water); }
  .week-mark { stroke: #7fd3ec; stroke-width: 0.8; stroke-dasharray: 2 2; }
  .lane-guide { stroke: var(--lane-blue); stroke-width: 2.2; }
  .lane-cap { stroke: var(--pool-navy); stroke-width: 2.2; }
  .rope-red { stroke: var(--rope-red); stroke-width: 3.5; stroke-dasharray: 8 4; }
  .rope-orange { stroke: var(--rope-orange); stroke-width: 3.5; stroke-dasharray: 8 4; }
  .start-block { fill: var(--tag-yellow); stroke: #b3a600; stroke-width: 0.5; }
  .swimmer { fill: #e9c49a; opacity: 0.9; }
  .no-diving { font-family: "Roboto", sans-serif; font-size: 7.5px; fill: var(--warning-red); letter-spacing: 0.3px; }
  .week-label { font-family: "Roboto", sans-serif; font-size: 10px; fill: #333; }
  .date-chip { fill: url(#chipFade); stroke: var(--ink); stroke-width: 0.7; }
  .chip-label { font-family: "Roboto", sans-serif; font-size: 6.5px; fill: var(--ink); }
  .winner-box { fill: var(--paper); stroke: var(--ink); stroke-width: 1.6; }
  .whistle { fill: var(--whistle-grey); }
  .trophy { fill: var(--trophy-gold); }
  .flag { fill: var(--flag-grey); }
</style>
</head>
<body>
<svg class="poster" viewBox="0 0 801 801" xmlns="http://www.w3.org/2000/svg">
  <defs>
    <linearGradient id="chipFade" x1="0" x2="1">
      <stop offset="0%" stop-color="#ffffff"/>
      <stop offset="100%" stop-color="#6fc4ea"/>
    </linearGradient>
  </defs>

  <rect class="band" x="0" y="0" width="801" height="801"/>
  <rect class="canvas-bg" x="0" y="47" width="801" height="705"/>

  <!-- poster frame and header tab -->
  <rect class="frame" x="5" y="116" width="790" height="563"/>
  <path class="fold-line" d="M5 207 H280 L310 116 M490 116 L520 207 H795"/>

  <g class="header">
    <text class="title" x="400" y="168" text-anchor="middle">LAP LEADERS</text>
    <text class="title" x="400" y="192" text-anchor="middle">RACE</text>
  </g>

  <!-- swimmers name column -->
  <g class="swimmer-names">
    <rect class="side-panel" x="15" y="238" width="60" height="360"/>
    <rect class="tag" x="16" y="223" width="57" height="15"/>
    <text class="tag-label" x="44.5" y="233.5" text-anchor="middle">SWIMMERS</text>
    <rect class="entry-field" x="27" y="262" width="39" height="8"/>
    <rect class="entry-field" x="27" y="295" width="39" height="8"/>
    <rect class="entry-field" x="27" y="328" width="39" height="8"/>
    <rect class="entry-field" x="27" y="361" width="39" height="8"/>
    <rect class="entry-field" x="27" y="394" width="39" height="8"/>
    <rect class="entry-field" x="27" y="428" width="39" height="8"/>
    <rect class="entry-field" x="27" y="461" width="39" height="8"/>
    <rect class="entry-field" x="27" y="494" width="39" height="8"/>
    <rect class="entry-field" x="27" y="527" width="39" height="8"/>
    <rect class="entry-field" x="27" y="560" width="39" height="8"/>
  </g>

  <!-- weeks column -->
  <g class="week-tally">
    <rect class="side-panel" x="729" y="236" width="60" height="362"/>
    <rect class="tag" x="730" y="221" width="58" height="15"/>
    <text class="tag-label" x="759" y="231.5" text-anchor="middle">WEEKS</text>
    <g>
      <rect class="entry-field" x="733" y="260" width="52" height="10"/><text class="week-num" x="735" y="268">1</text>
      <rect class="entry-field" x="733" y="294" width="52" height="10"/><text class="week-num" x="735" y="302">2</text>
      <rect class="entry-field" x="733" y="329" width="52" height="10"/><text class="week-num" x="735" y="337">3</text>
      <rect class="entry-field" x="733" y="362" width="52" height="10"/><text class="week-num" x="735" y="370">4</text>
      <rect class="entry-field" x="733" y="396" width="52" height="10"/><text class="week-num" x="735" y="404">5</text>
      <rect class="entry-field" x="733" y="430" width="52" height="10"/><text class="week-num" x="735" y="438">6</text>
      <rect class="entry-field" x="733" y="462" width="52" height="10"/><text class="week-num" x="735" y="470">7</text>
      <rect class="entry-field" x="733" y="494" width="52" height="10"/><text class="week-num" x="735" y="502">8</text>
      <rect class="entry-field" x="733" y="528" width="52" height="10"/><text class="week-num" x="735" y="536">9</text>
      <rect class="entry-field" x="733" y="562" width="52" height="10"/><text class="week-num" x="735" y="570">10</text>
    </g>
  </g>

  <!-- pool -->
  <g class="pool">
    <rect class="pool-surround" x="82" y="226" width="640" height="376"/>
    <rect class="pool-edge" x="92" y="233" width="608" height="361"/>
    <rect class="pool-lip" x="98" y="238" width="596" height="351"/>
    <rect class="water" x="104" y="243" width="588" height="343"/>

    <g class="week-marks">
      <line class="week-mark" x1="166" y1="243" x2="166" y2="586"/>
      <line class="week-mark" x1="223" y1="243" x2="223" y2="586"/>
      <line class="week-mark" x1="280" y1="243" x2="280" y2="586"/>
      <line class="week-mark" x1="338" y1="243" x2="338" y2="586"/>
      <line class="week-mark" x1="395" y1="243" x2="395" y2="586"/>
      <line class="week-mark" x1="453" y1="243" x2="453" y2="586"/>
      <line class="week-mark" x1="510" y1="243" x2="510" y2="586"/>
      <line class="week-mark" x1="568" y1="243" x2="568" y2="586"/>
      <line class="week-mark" x1="625" y1="243" x2="625" y2="586"/>
    </g>

    <g class="lane-guides">
      <line class="lane-guide" x1="120" y1="265" x2="678" y2="265"/>
      <line class="lane-guide" x1="120" y1="299" x2="678" y2="299"/>
      <line class="lane-guide" x1="120" y1="332" x2="678" y2="332"/>
      <line class="lane-guide" x1="120" y1="366" x2="678" y2="366"/>
      <line class="lane-guide" x1="120" y1="399" x2="678" y2="399"/>
      <line class="lane-guide" x1="120" y1="432" x2="678" y2="432"/>
      <line class="lane-guide" x1="120" y1="465" x2="678" y2="465"/>
      <line class="lane-guide" x1="120" y1="497" x2="678" y2="497"/>
      <line class="lane-guide" x1="120" y1="530" x2="678" y2="530"/>
      <line class="lane-guide" x1="120" y1="565" x2="678" y2="565"/>
    </g>
    <g class="lane-caps">
      <path class="lane-cap" d="M120 259v12M678 259v12M120 293v12M678 293v12M120 326v12M678 326v12M120 360v12M678 360v12M120 393v12M678 393v12M120 426v12M678 426v12M120 459v12M678 459v12M120 491v12M678 491v12M120 524v12M678 524v12M120 559v12M678 559v12"/>
    </g>

    <g class="lane-ropes">
      <line class="rope-red" x1="110" y1="282" x2="692" y2="282"/>
      <line class="rope-orange" x1="110" y1="316" x2="692" y2="316"/>
      <line class="rope-red" x1="110" y1="349" x2="692" y2="349"/>
      <line class="rope-orange" x1="110" y1="382" x2="692" y2="382"/>
      <line class="rope-red" x1="110" y1="415" x2="692" y2="415"/>
      <line class="rope-orange" x1="110" y1="448" x2="692" y2="448"/>
      <line class="rope-red" x1="110" y1="481" x2="692" y2="481"/>
      <line class="rope-orange" x1="110" y1="512" x2="692" y2="512"/>
      <line class="rope-red" x1="110" y1="546" x2="692" y2="546"/>
    </g>

    <g class="start-blocks">
      <rect class="start-block" x="88" y="259" width="15" height="13"/>
      <rect class="start-block" x="88" y="292" width="15" height="13"/>
      <rect class="start-block" x="88" y="325" width="15" height="13"/>
      <rect class="start-block" x="88" y="358" width="15" height="13"/>
      <rect class="start-block" x="88" y="391" width="15" height="13"/>
      <rect class="start-block" x="88" y="425" width="15" height="13"/>
      <rect class="start-block" x="88" y="458" width="15" height="13"/>
      <rect class="start-block" x="88" y="490" width="15" height="13"/>
      <rect class="start-block" x="88" y="521" width="15" height="13"/>
      <rect class="start-block" x="88" y="555" width="15" height="13"/>
    </g>

    <g class="swimmer-markers">
      <rect class="swimmer" x="290" y="257" width="43" height="15" rx="7" role="img" aria-label="Swimmer marker, lane 1"/>
      <rect class="swimmer" x="403" y="290" width="44" height="15" rx="7" role="img" aria-label="Swimmer marker, lane 2"/>
      <rect class="swimmer" x="461" y="324" width="44" height="15" rx="7" role="img" aria-label="Swimmer marker, lane 3"/>
      <rect class="swimmer" x="348" y="358" width="42" height="15" rx="7" role="img" aria-label="Swimmer marker, lane 4"/>
      <rect class="swimmer" x="230" y="391" width="45" height="15" rx="7" role="img" aria-label="Swimmer marker, lane 5"/>
      <rect class="swimmer" x="345" y="424" width="45" height="15" rx="7" role="img" aria-label="Swimmer marker, lane 6"/>
      <rect class="swimmer" x="290" y="457" width="43" height="15" rx="7" role="img" aria-label="Swimmer marker, lane 7"/>
      <rect class="swimmer" x="174" y="489" width="43" height="15" rx="7" role="img" aria-label="Swimmer marker, lane 8"/>
      <rect class="swimmer" x="113" y="520" width="47" height="15" rx="7" role="img" aria-label="Swimmer marker, lane 9"/>
      <rect class="swimmer" x="517" y="558" width="45" height="15" rx="7" role="img" aria-label="Swimmer marker, lane 10"/>
    </g>

    <g class="pool-signs">
      <text class="no-diving" transform="translate(719 287) rotate(-90)">NO DIVING</text>
      <text class="no-diving" transform="translate(719 430) rotate(-90)">NO DIVING</text>
      <text class="no-diving" transform="translate(719 587) rotate(-90)">NO DIVING</text>
    </g>
  </g>

  <g class="week-labels">
    <text class="week-label" x="135" y="612" text-anchor="middle">WEEK 1</text>
    <text class="week-label" x="196" y="612" text-anchor="middle">WEEK 2</text>
    <text class="week-label" x="253" y="612" text-anchor="middle">WEEK 3</text>
    <text class="week-label" x="311" y="612" text-anchor="middle">WEEK 4</text>
    <text class="week-label" x="368" y="612" text-anchor="middle">WEEK 5</text>
    <text class="week-label" x="426" y="612" text-anchor="middle">WEEK 6</text>
    <text class="week-label" x="483" y="612" text-anchor="middle">WEEK 7</text>
    <text class="week-label" x="540" y="612" text-anchor="middle">WEEK 8</text>
    <text class="week-label" x="598" y="612" text-anchor="middle">WEEK 9</text>
    <text class="week-label" x="661" y="612" text-anchor="middle">WEEK 10</text>
  </g>

  <!-- footer: start, winner, finish -->
  <g class="footer">
    <ellipse class="whistle" cx="158" cy="646" rx="26" ry="20" role="img" aria-label="Referee whistle illustration"/>
    <path class="date-chip" d="M186 636 H269 L265 652 H183 Z"/>
    <text class="chip-label" x="191" y="647">START DATE:</text>

    <path class="winner-box" d="M353 625 H510 L504 650 H348 Z"/>
    <rect class="trophy" x="326" y="616" width="34" height="54" rx="6" role="img" aria-label="Gold winner's trophy illustration"/>
    <path class="date-chip" d="M362 651 H485 L482 661 H360 Z"/>
    <text class="chip-label" x="368" y="659">AND THE WINNER IS...</text>

    <rect class="flag" x="550" y="622" width="34" height="46" rx="4" role="img" aria-label="Chequered finish flag illustration"/>
    <path class="date-chip" d="M590 632 H680 L676 648 H587 Z"/>
    <text class="chip-label" x="595" y="643">FINISH DATE:</text>
  </g>
</svg>
</body>
</html>
```